Vorlen Holdings Web Design

Vorlen Holdings Limited Shenzhen

This project is a 10 page launch website.
Our client is seeking a contemporary homepage design for a Holdings company. Once we are happy with the homepage design and select designer we will request a secondary page design.

Please see attached company LOGO for an idea of style, it incorporates the traditional Chinese furniture lattice work. The Quillmoss website is one of our clients favorite so we would like to see a similar homepage design to this website.

Use the websites below for reference purpose. The first two are Chinese and the second two are international. We would like to see elements of both but more focus on international design.

http://www.evergrande.com/http://www.kelrunagroup.com/pub/default.aspx http://www.quillmoss.com/zh/maldives_tornelvaru/
http://www.brevatte-london.com
http://media-cache-ec0.snapwelkimg.com/originals/28/d6/47/28d64786e0e66d5b6795249c7ee0d2b8.jpg

Company Background
VORLEN HOLDINGS, located in Qianhai, China, is a new real-estate project operator, structuring urban-rural real-estate investment and development, and industrial fund investment. The company also invests in supply chain management and supporting infrastructures. To create new spaces and livable cities Vorlen Holdings develop win-win strategic partnerships with a number of institutions. Currently cooperating with Tianjing West Luorenpo, China urban and rural integrated demonstration.

Target Market(s)

B2B property investment. Target market customers are senior level management/decision makers of large corporations. Focusing geographically on the domestic market first and expanding internationally in 2nd and 3rd years.

Industry/Entity Type

Investment

Requirements
Must have
• Since this is a new company, we would like to the website representing growth and power, E.g. like a growing tree.
Should not have
• Low-level vectors such as curency symbols, American dollar.

```html
<!DOCTYPE html>
<html lang="en">
<head>
<meta charset="utf-8">
<title>Vorlen Holdings</title>
<link rel="stylesheet" href="https://fonts.googleapis.com/css2?family=Questrial&family=Roboto+Condensed:wght@300;400&family=Ubuntu:ital,wght@0,400;0,500;0,700;1,400&display=swap">
<style>
:root{
  --gold:#c8961f;
  --orange:#f3a10c;
  --orange-dark:#d98600;
  --ink:#2a2a2a;
  --text:#555;
  --muted:#888;
  --light-bg:#f6f6f6;
  --dark-bg:#1f1f1f;
  --footer-bg:#2b2b2b;
  --bar-bg:#1b1b1b;
  --white:#fff;
  --line:#d9d9d9;
}
*{margin:0;padding:0;box-sizing:border-box}
html,body{width:668px;height:1200px;overflow:hidden}
body{position:relative;font-family:"Ubuntu",sans-serif;color:var(--text);background:var(--white)}
.abs{position:absolute}

/* header */
.site-header{position:absolute;left:0;top:0;width:668px;height:60px;background:var(--white);border-top:3px solid #eee}
.brand{position:absolute;left:83px;top:6px;width:62px;text-align:center}
.brand-mark{display:block;width:34px;height:34px;margin:0 auto;border-radius:50%;background:var(--gold)}
.brand-name{display:block;margin-top:3px;font-size:7px;color:var(--gold);white-space:nowrap;font-family:"Ubuntu",sans-serif}
.search{position:absolute;left:407px;top:4px;width:133px;height:17px;border:1px solid #ddd;background:#fff;box-shadow:0 1px 2px rgba(0,0,0,.15)}
.search span{position:absolute;left:6px;top:4px;font-size:6.5px;color:#999}
.search svg{position:absolute;right:4px;top:3px}
.lang{position:absolute;left:546px;top:4px;width:32px;height:17px;border:1px solid #ddd;background:#f4f4f4}
.lang i{position:absolute;left:4px;top:5px;width:10px;height:7px;background:#5570a8}
.lang svg{position:absolute;right:5px;top:6px}
.nav{position:absolute;top:33px;left:298px;display:flex;align-items:center;list-style:none}
.nav li{font-size:9.5px;font-weight:500;color:#333;letter-spacing:.2px}
.nav .active{background:linear-gradient(#ffb322,var(--orange-dark));color:#fff;width:49px;height:20px;line-height:20px;text-align:center;border-radius:2px}
.nav li+li{margin-left:18px}

/* hero */
.hero{position:absolute;left:0;top:60px;width:668px;height:350px;
  background:radial-gradient(ellipse at 70% 25%,#8a6a3a 0%,#3d2d1e 35%,transparent 60%),
             linear-gradient(180deg,#3a2f28 0%,#22201e 55%,#141414 100%)}
.hero-title{position:absolute;left:0;width:668px;top:322px;text-align:center;font-family:"Questrial",sans-serif;font-size:39px;color:#fff;letter-spacing:.5px}
.hero-sub{position:absolute;left:0;width:668px;top:368px;text-align:center;font-family:"Questrial",sans-serif;font-size:17px;color:#fff}
.dots{display:flex;gap:3px}
.dots i{width:5px;height:5px;border-radius:50%;background:#fff;border:1px solid #ccc}
.dots i.on{background:var(--gold);border-color:var(--gold)}
.hero .dots{position:absolute;left:322px;top:335px}

/* intro */
.intro{position:absolute;left:0;top:410px;width:668px;height:186px;background:var(--light-bg)}
.h2{font-family:"Roboto Condensed",sans-serif;font-weight:400;color:var(--ink)}
.intro-title{position:absolute;left:83px;top:27px;font-size:18px}
.rule{position:absolute;height:1px;background:var(--line)}
.rule b{position:absolute;left:0;top:-1px;width:37px;height:2px;background:var(--gold)}
.copy{font-size:7.4px;line-height:12px;color:#555}
.intro .copy{position:absolute;left:83px;width:324px}
.news{position:absolute;left:441px;top:30px;width:143px;height:118px;background:#fff;border:1px solid #e2e2e2;box-shadow:0 1px 3px rgba(0,0,0,.08)}
.news-tabs{display:flex;height:15px;margin:0 0 0 0;border-bottom:1px solid #e2e2e2}
.news-tabs span{font-size:7.5px;padding:3px 7px 0}
.news-tabs .tab-on{color:#333;background:#fff}
.news-tabs .tab-off{color:#999;background:#eee}
.news-item{padding:8px 11px 0}
.news-item h4{font-weight:400;font-style:italic;font-size:6.3px;color:var(--gold)}
.news-item time{display:block;font-style:italic;font-size:5.6px;color:#aaa;margin:2px 0 3px}
.news-item p{font-style:italic;font-size:6px;line-height:8px;color:#666}
.news-item+.news-item{border-top:1px solid #eee;margin-top:6px}
.intro .dots{position:absolute;left:441px;top:154px}
.intro .dots i{background:#fff;border-color:#bbb}
.intro .dots i.on{background:var(--gold);border-color:var(--gold)}

/* projects */
.projects{position:absolute;left:0;top:596px;width:668px;height:275px;
  background:linear-gradient(90deg,#262626 0%,#1c1c1c 40%,#232323 100%)}
.projects-title{position:absolute;left:83px;top:55px;font-size:17px;color:var(--gold)}
.projects .rule{background:#444}
.project-name{position:absolute;left:83px;top:95px;font-size:10px;font-weight:700;color:#fff}
.projects .copy{position:absolute;left:83px;width:142px;color:#ccc}
.project-photo{position:absolute;left:241px;top:59px;width:342px;height:161px;
  background:linear-gradient(180deg,#9fb7c6 0%,#b6c3c8 22%,#b8464f 38%,#e8e4dc 52%,#5c8a3a 68%,#3f6f2a 100%)}
.projects .dots{position:absolute;left:83px;top:212px}

/* testimonial */
.testimonial{position:absolute;left:0;top:871px;width:668px;height:187px;background:var(--light-bg)}
.quote-mark{position:absolute;left:86px;top:32px}
.quote{position:absolute;left:120px;top:36px;width:464px;font-style:italic;font-size:7.4px;line-height:12px;color:#555}
.quote-rule{position:absolute;left:120px;top:82px}
.avatar{position:absolute;left:123px;top:104px;width:44px;height:44px;border-radius:50%;border:2px solid #fff;box-shadow:0 0 0 1px #ccc;background:linear-gradient(180deg,#a7c4dc,#3a4b63)}
.person{position:absolute;left:183px;top:113px;font-family:"Roboto Condensed",sans-serif;font-size:11px;color:var(--gold)}
.role{position:absolute;left:184px;top:127px;font-size:6.5px;color:#666}
.testimonial .dots{position:absolute;left:557px;top:131px}
.testimonial .dots i{background:#fff;border-color:#bbb}
.testimonial .dots i.on{background:var(--gold);border-color:var(--gold)}

/* footer */
.site-footer{position:absolute;left:0;top:1058px;width:668px;height:116px;background:var(--footer-bg)}
.col-title{position:absolute;top:14px;font-family:"Roboto Condensed",sans-serif;font-size:12px;color:var(--gold)}
.col-sep{position:absolute;top:8px;width:1px;height:108px;background:#3c3c3c}
.links{position:absolute;top:40px;list-style:none}
.links li{font-size:6.5px;line-height:11.6px;color:#bbb;padding-left:9px;position:relative}
.links li::before{content:"";position:absolute;left:0;top:4.5px;width:3px;height:3px;border-radius:50%;background:#999}
.links.plain li{padding-left:10px}
.news-desc{position:absolute;left:336px;top:42px;width:250px;font-size:6.5px;line-height:11px;color:#bbb}
.subscribe{position:absolute;left:336px;top:73px;width:246px;height:30px;background:#1b1b1b;border-radius:2px}
.subscribe .field{position:absolute;left:6px;top:4px;width:185px;height:19px;background:#fff;border-radius:2px;font-size:6.5px;color:#888;padding:6px 6px}
.subscribe .btn{position:absolute;left:196px;top:4px;width:45px;height:19px;background:var(--orange);border-radius:2px;font-size:6.5px;color:#222;text-align:center;line-height:19px}
.bottom-bar{position:absolute;left:0;top:1174px;width:668px;height:26px;background:var(--bar-bg)}
.copyright{position:absolute;left:83px;top:9px;font-size:6.5px;color:#aaa}
.social{position:absolute;left:527px;top:4px;display:flex;gap:4px}
.social i{width:16px;height:16px;border-radius:50%}
.social .s1{background:#3b5b99}
.social .s2{background:#2ea3dd}
.social .s3{background:#d2453a}
</style>
</head>
<body>

<header class="site-header">
  <div class="brand">
    <span class="brand-mark"></span>
    <span class="brand-name">Vorlen Holdings</span>
  </div>
  <div class="search">
    <span>Search</span>
    <svg width="9" height="9" viewBox="0 0 9 9"><circle cx="3.6" cy="3.6" r="2.7" fill="none" stroke="#555" stroke-width="1.1"/><line x1="5.6" y1="5.6" x2="8.4" y2="8.4" stroke="#555" stroke-width="1.3"/></svg>
  </div>
  <div class="lang"><i></i><svg width="6" height="4" viewBox="0 0 6 4"><path d="M0 0h6L3 4z" fill="#555"/></svg></div>
  <ul class="nav">
    <li class="active">HOME</li>
    <li>ABOUT</li>
    <li>SERVICES</li>
    <li>BLOG</li>
    <li>CONTACT</li>
  </ul>
</header>

<section class="hero" role="img" aria-label="Three smiling business people in suits before blurred city lights at night">
  <h1 class="hero-title abs" style="top:262px">Morbi tristique senectus</h1>
  <p class="hero-sub abs" style="top:307px">Pellentesque habitant morbi tristique netus et malesuada</p>
  <div class="dots"><i class="on"></i><i></i><i></i><i></i></div>
</section>

<section class="intro">
  <h2 class="h2 intro-title">Varius turpis ut neque scelerisque</h2>
  <div class="rule" style="left:83px;top:54px;width:322px"><b></b></div>
  <p class="copy" style="top:66px">Consectetur adipiscing elit. Etiam felis ante, laoreet vel mi commodo, dapibus porta lectus. Sed elementum scelerisque nunc, non accumsan est pretium nec. Nunc ac lacinia diam, in ultrices orci. Lorem ipsum dolor sit amet, consectetur adipiscing elit. Pellentesque habitant morbi tristique senectus et netus et malesuada fames ac turpis egestas. Pellentesque habitant morbi tristique senectus et netus et malesuada fames ac turpis egestas.</p>
  <p class="copy" style="top:133px">Consectetur adipiscing elit. Etiam felis ante, laoreet vel mi commodo, dapibus porta lectus. Sed elementum scelerisque nunc, non accumsan est pretium nec.</p>

  <aside class="news">
    <div class="news-tabs"><span class="tab-on">News</span><span class="tab-off">Reviews &amp; Awards</span></div>
    <article class="news-item">
      <h4>Condimentum nisi eu convallis</h4>
      <time>02 Jun 2014</time>
      <p>Lorem ipsum dolor sit amet, consectetur adipiscing elit. Etiam felis ante.....</p>
    </article>
    <article class="news-item">
      <h4>Condimentum nisi eu convallis</h4>
      <time>02 Jun 2014</time>
      <p>Lorem ipsum dolor sit amet, consectetur adipiscing elit. Etiam felis ante.....</p>
    </article>
  </aside>
  <div class="dots"><i class="on"></i><i></i><i></i><i></i></div>
</section>

<section class="projects">
  <h2 class="h2 projects-title">Feature Projects</h2>
  <div class="rule" style="left:83px;top:83px;width:142px"><b></b></div>
  <h3 class="project-name">Lectus Scelerisque</h3>
  <p class="copy" style="top:115px">Consectetur adipiscing elit. Etiam felis ante, laoreet vel mi commodo, dapibus porta lectus scelerisque.</p>
  <p class="copy" style="top:157px">Consectetur adipiscing elit. Etiam felis ante, laoreet vel mi commodo, dapibus porta lectus scelerisque nunc accumsan est pretium nec.</p>
  <div class="project-photo" role="img" aria-label="White villa with red roofs among green trees beside the sea"></div>
  <div class="dots"><i class="on"></i><i></i><i></i><i></i></div>
</section>

<section class="testimonial">
  <svg class="quote-mark" width="22" height="20" viewBox="0 0 22 20"><path d="M0 20V9C0 3 3 0 8 0v4C5 4 4 6 4 9h5v11zM13 20V9c0-6 3-9 8-9v4c-3 0-4 2-4 5h5v11z" fill="#d6d6d6"/></svg>
  <p class="quote">Pellentesque habitant morbi tristique senectus et netus et mesuada fames ac turpis egestas. Pellenue habitant morbi tristique senectus et netus et malesuada fames ac turpis egestas Quisque urna mi, faucibus at magna vel, venenatis ornare sem&nbsp; Pellentesque habitant morbi tristique senectus et netus et malesuada fames ac turpis egestas.</p>
  <svg class="quote-rule" width="464" height="8" viewBox="0 0 464 8"><path d="M0 .5H22l4 5 4-5H464" fill="none" stroke="#cfcfcf"/></svg>
  <div class="avatar" role="img" aria-label="Portrait of a client in a suit"></div>
  <p class="person">Consectetur Adipiscing</p>
  <p class="role">Lorem ipsum</p>
  <div class="dots"><i class="on"></i><i></i><i></i><i></i></div>
</section>

<footer class="site-footer">
  <h4 class="col-title" style="left:83px">Our Services</h4>
  <ul class="links" style="left:83px">
    <li>Consectetur adipiscing</li>
    <li>Etiam felis ante laoreet</li>
    <li>Commodo dapibus porta</li>
    <li>Lectus Sed elementum</li>
    <li>Scelerisque accumsan</li>
  </ul>
  <span class="col-sep" style="left:185px"></span>
  <h4 class="col-title" style="left:202px">Condimentum est</h4>
  <ul class="links" style="left:202px;width:104px">
    <li>Pellentesque habitant morbi tristique senectus et netus et malesuada fames ac turpis egestas. Pellentesque habitant morbi tristique</li>
  </ul>
  <span class="col-sep" style="left:315px"></span>
  <h4 class="col-title" style="left:336px">Subscribe our newsletter</h4>
  <p class="news-desc">Habitant morbi tristique senectus et netus et malesuada fames ac turpis egestas. Quisque urna mi, faucibus at magna vel, venenatis ornare sem.</p>
  <form class="subscribe">
    <div class="field">Enter your email here</div>
    <div class="btn">SUBSCRIBE</div>
  </form>
</footer>

<div class="bottom-bar">
  <p class="copyright">Vorlen Holdings © All rights reserved.</p>
  <div class="social"><i class="s1"></i><i class="s2"></i><i class="s3"></i></div>
</div>

</body>
</html>
```